Business Card Design

We are looking for a double sided business card.

On one side would be our logo

On the Other Side

Martin Kolby
Sales and Marketing

Phone/Text Logo and 530-418-2763
Email Logo and info@plumvalepets.com
Website Logo and www.plumvalepets.com
Facebook Logo and plumvale pets
Instagram Logo and plumvale_pets

Target Market(s)

Pet owners

Contact Information for Business Card

In project description

Requirements
Must have
• Logo

```html
<!DOCTYPE html>
<html lang="en">
<head>
<meta charset="utf-8">
<title>Plumvale Pets – Business Card</title>
<link rel="stylesheet" href="https://fonts.googleapis.com/css2?family=Michroma&family=Roboto:wght@400;500;700&display=swap">
<style>
  :root {
    --stage: #3b342d;
    --card-dark: #1c1c1c;
    --card-dark-edge: #111111;
    --orange: #f29a1d;
    --orange-deep: #e8790f;
    --orange-light: #ffc94a;
    --ink: #222222;
    --white: #ffffff;
    --muted: #cfcfcf;
  }
  * { box-sizing: border-box; margin: 0; padding: 0; }
  html, body { width: 900px; height: 1200px; overflow: hidden; }
  body {
    background: var(--stage);
    font-family: "Roboto", Arial, sans-serif;
    position: relative;
  }
  .card {
    position: absolute;
    left: 70px;
    width: 760px;
    height: 460px;
    border-radius: 22px;
    overflow: hidden;
    box-shadow: 0 10px 30px rgba(0,0,0,.45);
  }
  /* Contact side */
  .card--contact {
    top: 70px;
    background: radial-gradient(ellipse at 60% 40%, #262626 0%, var(--card-dark) 55%, var(--card-dark-edge) 100%);
    color: var(--white);
  }
  .brand {
    position: absolute;
    left: 40px;
    top: 70px;
    width: 380px;
    display: flex;
    align-items: center;
    gap: 14px;
  }
  .brand__mark {
    width: 30px; height: 30px;
    background: var(--orange);
    flex: none;
  }
  .brand__name {
    font-family: "Michroma", sans-serif;
    font-size: 34px;
    line-height: 1.15;
    color: var(--white);
    letter-spacing: 1px;
  }
  .person {
    position: absolute;
    right: 40px;
    top: 30px;
    text-align: left;
  }
  .person__name {
    font-weight: 700;
    font-size: 27px;
    color: var(--orange);
  }
  .person__role {
    font-size: 17px;
    color: var(--white);
    margin-top: 4px;
  }
  .person__tab {
    position: absolute;
    right: 0; top: 34px;
    width: 22px; height: 30px;
    background: var(--orange);
  }
  .contacts {
    position: absolute;
    left: 40px;
    top: 310px;
    list-style: none;
  }
  .contacts li, .social li {
    display: flex;
    align-items: center;
    gap: 14px;
    font-size: 17px;
    color: var(--muted);
    height: 36px;
  }
  .icon {
    width: 24px; height: 24px;
    border-radius: 4px;
    background: var(--orange);
    display: flex; align-items: center; justify-content: center;
    flex: none;
  }
  .icon svg { width: 15px; height: 15px; }
  .follow {
    position: absolute;
    left: 470px;
    top: 274px;
  }
  .follow__title {
    font-weight: 700;
    font-size: 19px;
    color: var(--orange);
    letter-spacing: 1px;
    margin-bottom: 6px;
  }
  .social { list-style: none; }
  .icon--plain { width: 24px; height: 24px; border-radius: 4px; background: var(--orange); flex: none; }

  /* Logo side */
  .card--logo {
    top: 670px;
    border-radius: 40px;
    background: radial-gradient(ellipse at 50% 45%, var(--orange-light) 0%, var(--orange) 50%, var(--orange-deep) 100%);
    display: flex;
    flex-direction: column;
    align-items: center;
    justify-content: center;
    gap: 28px;
  }
  .logo-lockup {
    display: flex;
    align-items: center;
    gap: 20px;
  }
  .logo-lockup .brand__mark { width: 40px; height: 40px; background: var(--ink); }
  .logo-lockup .brand__name { font-size: 48px; color: var(--ink); }
  .website {
    font-family: "Michroma", sans-serif;
    font-size: 22px;
    letter-spacing: 4px;
    color: var(--ink);
    text-transform: uppercase;
  }
</style>
</head>
<body>

<section class="card card--contact">
  <div class="brand">
    <span class="brand__mark"></span>
    <span class="brand__name">PLUMVALE PETS</span>
  </div>

  <div class="person">
    <p class="person__name">Martin Kolby</p>
    <p class="person__role">Sales and Marketing</p>
  </div>
  <span class="person__tab"></span>

  <ul class="contacts">
    <li>
      <span class="icon"><svg viewBox="0 0 24 24"><path fill="#1c1c1c" d="M6.6 10.8a15 15 0 0 0 6.6 6.6l2.2-2.2c.3-.3.7-.4 1-.2 1.1.4 2.3.6 3.6.6.6 0 1 .4 1 1V20c0 .6-.4 1-1 1A17 17 0 0 1 3 4c0-.6.4-1 1-1h3.5c.6 0 1 .4 1 1 0 1.3.2 2.5.6 3.6.1.3 0 .7-.2 1z"/></svg></span>
      (530)418-2763
    </li>
    <li>
      <span class="icon"><svg viewBox="0 0 24 24"><rect x="3" y="5" width="18" height="14" rx="1" fill="none" stroke="#1c1c1c" stroke-width="2.2"/><path d="M3 6l9 7 9-7" fill="none" stroke="#1c1c1c" stroke-width="2.2"/></svg></span>
      info@plumvalepets.com
    </li>
    <li>
      <span class="icon"><svg viewBox="0 0 24 24"><circle cx="12" cy="12" r="9" fill="none" stroke="#1c1c1c" stroke-width="2"/><path d="M3 12h18M12 3c3 3 3 15 0 18M12 3c-3 3-3 15 0 18" fill="none" stroke="#1c1c1c" stroke-width="1.8"/></svg></span>
      www.plumvalepets.com
    </li>
  </ul>

  <div class="follow">
    <p class="follow__title">FOLLOW US</p>
    <ul class="social">
      <li><span class="icon--plain"></span>@plumvale pets</li>
      <li><span class="icon--plain"></span>@plumvale_pets</li>
    </ul>
  </div>
</section>

<section class="card card--logo">
  <div class="logo-lockup">
    <span class="brand__mark"></span>
    <span class="brand__name">PLUMVALE PETS</span>
  </div>
  <p class="website">www.plumvalepets.com</p>
</section>

</body>
</html>
```